84k | SOLUTIONS Biz Card Design

Brightmoor Solutions, LLC
84k | HOME INSPECTIONS
84k | ENVIRONMENTAL TESTING
84k | THERMOGRAPHY IMAGING
(Would like progressive design, maybe use 84k as a logo or part of logo; want to reflect healthy environments, incorporating sun, or blue skies, etc.; primary colors, one side or two is acceptable)
Updates

I'm very partial to the simple modern fonts such as Helvetica or Museo Sans 500 or the new one I've recently seen that's like Helvetica with attitude. Added Tuesday, May 5, 2015

Target Market(s)

Home owners and realtors

Industry/Entity Type

Progressive

Contact Information for Business Card

Ned Forsythe, President/CEO
NedForsythe@84kSolutions.example
www.84kSolutions.example
555.730.4418
555.730.4419 fax

Font styles to use
Other font styles liked:
• Fabrica, Helvetica, Arial, Nevis, Nexa

Colors
0355a3
ec1f27
ffffff
fbed22
ffc214
9bcb3b

Requirements
Must have
• Professional yet bright colors design. Don't want to look too mom and pop.
Nice to have
• Use '84k' to create a logo.
Should not have
• Not too busy, make two-sided if there's not enough white space.

```html
<!DOCTYPE html>
<html lang="en">
<head>
<meta charset="utf-8">
<title>84k Solutions Business Card</title>
<link rel="stylesheet" href="https://fonts.googleapis.com/css2?family=Nunito+Sans:wght@400;600;800&display=swap">
<style>
  :root {
    --page: #eee9dc;
    --leaf-green: #9bcb3b;
    --sky-blue: #85c2ea;
    --sun-yellow: #ffc214;
    --sun-soft: #fbed22;
    --paper: #ffffff;
    --ink: #4a5a3a;
  }
  * { box-sizing: border-box; margin: 0; padding: 0; }
  html, body { width: 1200px; height: 1000px; overflow: hidden; }
  body {
    background: var(--page);
    font-family: "Nunito Sans", Helvetica, Arial, sans-serif;
    position: relative;
  }
  .card {
    position: absolute;
    left: 250px;
    width: 700px;
    height: 400px;
    overflow: hidden;
    box-shadow: 0 6px 18px rgba(0,0,0,0.12);
  }

  /* Back side */
  .card-back { top: 60px; background: var(--leaf-green); }
  .contact {
    position: absolute;
    right: 70px;
    top: 60px;
    text-align: right;
    color: var(--ink);
  }
  .contact-name { color: var(--paper); font-weight: 800; font-size: 30px; line-height: 1.1; }
  .contact-title { color: var(--paper); font-weight: 400; font-size: 17px; margin-bottom: 34px; }
  .contact-line { font-size: 17px; line-height: 1.45; }
  .contact-line .label { margin-right: 8px; }
  .back-brand {
    position: absolute;
    left: 70px;
    bottom: 60px;
    color: var(--paper);
  }
  .back-brand .wordmark { font-size: 110px; font-weight: 800; line-height: 0.9; letter-spacing: -2px; }
  .back-brand .company { font-size: 18px; font-weight: 600; margin-top: 10px; }

  /* Front side */
  .card-front { top: 540px; background: var(--paper); }
  .band-sky { position: absolute; left: 0; top: 0; width: 100%; height: 40px; background: var(--sky-blue); }
  .band-ground {
    position: absolute; left: 0; bottom: 0; width: 100%; height: 86px;
    background: var(--leaf-green);
    color: var(--paper);
    font-weight: 800; font-size: 22px;
    display: flex; align-items: center; justify-content: center;
    letter-spacing: 0.5px;
  }
  .sun {
    position: absolute;
    left: 300px; top: 112px;
    width: 180px; height: 180px;
    border-radius: 50%;
    background: radial-gradient(circle, #fff6c4 0%, #fdf0a0 70%, #fbe88a 100%);
  }
  .front-brand {
    position: absolute;
    left: 160px; top: 78px;
    display: flex; align-items: center;
  }
  .front-brand .wordmark {
    color: var(--leaf-green);
    font-size: 150px; font-weight: 800; line-height: 1; letter-spacing: -3px;
  }
  .divider { width: 3px; height: 110px; background: var(--leaf-green); margin: 30px 18px 0 22px; }
  .services {
    list-style: none;
    color: var(--sun-yellow);
    font-size: 20px; font-weight: 600; line-height: 1.15;
    margin-top: 30px;
  }
  .front-company {
    position: absolute;
    left: 190px; top: 252px;
    color: var(--leaf-green);
    font-size: 21px; font-weight: 600;
  }
</style>
</head>
<body>
  <section class="card card-back">
    <div class="contact">
      <p class="contact-name">Ned Forsythe</p>
      <p class="contact-title">President/CEO</p>
      <p class="contact-line">NedForsythe@84kSolutions.example</p>
      <p class="contact-line">555.730.4418</p>
      <p class="contact-line"><span class="label">Fax</span>555.730.4419</p>
    </div>
    <div class="back-brand">
      <p class="wordmark">84k</p>
      <p class="company">Brightmoor Solutions, LLC</p>
    </div>
  </section>

  <section class="card card-front">
    <div class="band-sky"></div>
    <div class="sun"></div>
    <div class="front-brand">
      <p class="wordmark">84k</p>
      <span class="divider"></span>
      <ul class="services">
        <li>Home Inspections</li>
        <li>Environmental Testing</li>
        <li>Thermography Imaging</li>
      </ul>
    </div>
    <p class="front-company">Brightmoor Solutions, LLC</p>
    <div class="band-ground">www.84kSolutions.example</div>
  </section>
</body>
</html>
```